Willowmere Rites Studio creates individual, personalised ceremonies to celebrate weddings, naming days,coming of age, significant age, divorce and final resting rites. Ceremonies and meaningful rituals are created in collaboration with the individual to reflect their hopes and desires, how they will/have embrace/d their lives. The final design should have the logo (purple) on a white/silver background on the right hand side of the card. Name of business and contact details in red on a black background on the left
Updates

Hi All, have only just realised I have paid for a double sided card, yep, a newbie! Sorry to set the cat amongst the pigeons but could we put 'creating...... etc' on the back?

Target Market(s)

Couples marrying, renewing of vows, baby naming days, coming of age, significant age, divorce, funeral ceremonies. The target market predominantly will be couples marrying.

Industry/Entity Type

Business

Contact Information for Business Card

Willowmere Rites Studio, Tamsin Crowther, 0492-718305 willowmereritesstudio1@quillpost.net
"Crafting singular, bespoke occasions honouring journeys"

Font styles to use
Script

Colors
eb1f27
6b449b
f3f0f8

Requirements
Must have
• On initial entry, and now, the logo was not displayed in full - the bottom part was cut off - this needs to be in it's entirety. Colours as previously specified are non-negotiable. Font and placement of characters will be assessed as produced.
Should not have
• Telephone symbol, call us, director,grammatical symbols ( : )

```html
<!DOCTYPE html>
<html lang="en">
<head>
<meta charset="utf-8">
<title>Willowmere Rites Studio — Business Card</title>
<link rel="stylesheet" href="https://fonts.googleapis.com/css2?family=Great+Vibes&family=Italianno&display=swap">
<style>
  :root {
    --paper: #ffffff;
    --card-black: #000000;
    --brand-red: #eb1f27;
    --brand-purple: #6b449b;
    --silver-light: #f3f0f8;
    --silver-mid: #c9c6cc;
    --silver-dark: #5b5859;
  }
  html, body {
    margin: 0;
    padding: 0;
    width: 1200px;
    height: 741px;
    overflow: hidden;
    background: var(--paper);
  }
  .card {
    position: absolute;
    left: 13px;
    top: 19px;
    width: 1173px;
    height: 703px;
    background: var(--card-black);
    overflow: hidden;
  }
  .silver-panel {
    position: absolute;
    inset: 0;
    width: 1173px;
    height: 703px;
  }
  .details {
    position: absolute;
    left: 0;
    top: 0;
    width: 780px;
    height: 703px;
    color: var(--brand-red);
  }
  .details > * {
    position: absolute;
    margin: 0;
    white-space: nowrap;
    transform: translateX(-50%);
    font-weight: 400;
  }
  .business-name {
    left: 390px;
    top: 92px;
    font-family: "Great Vibes", cursive;
    font-size: 68px;
  }
  .tagline {
    left: 386px;
    top: 176px;
    font-family: "Italianno", cursive;
    font-size: 46px;
    line-height: 58px;
    letter-spacing: 5px;
    text-align: center;
  }
  .person-name {
    left: 370px;
    top: 312px;
    font-family: "Great Vibes", cursive;
    font-size: 72px;
  }
  .email {
    left: 376px;
    top: 428px;
    font-family: "Italianno", cursive;
    font-size: 54px;
    letter-spacing: 1px;
  }
  .phone {
    left: 375px;
    top: 508px;
    font-family: "Italianno", cursive;
    font-size: 60px;
    letter-spacing: 8px;
  }
  .brand-mark {
    position: absolute;
    left: 780px;
    top: 0;
    width: 373px;
    height: 703px;
  }
  .brand-dot {
    position: absolute;
    left: 115px;
    top: 215px;
    width: 150px;
    height: 150px;
    border-radius: 50%;
    background: var(--brand-purple);
  }
  .brand-name {
    position: absolute;
    left: 0;
    top: 500px;
    width: 373px;
    margin: 0;
    text-align: center;
    font-family: "Great Vibes", cursive;
    font-weight: 400;
    font-size: 50px;
    line-height: 70px;
    color: var(--brand-purple);
  }
</style>
</head>
<body>
  <main class="card">
    <svg class="silver-panel" viewBox="0 0 1173 703" aria-hidden="true">
      <defs>
        <linearGradient id="silver-sheen" x1="0" y1="0" x2="1" y2="0">
          <stop offset="0" stop-color="#f3f0f8"/>
          <stop offset="0.35" stop-color="#dedbe2"/>
          <stop offset="0.7" stop-color="#a9a6aa"/>
          <stop offset="1" stop-color="#5b5859"/>
        </linearGradient>
        <radialGradient id="silver-glow" cx="0.3" cy="0.5" r="0.6">
          <stop offset="0" stop-color="#ffffff" stop-opacity="0.6"/>
          <stop offset="1" stop-color="#ffffff" stop-opacity="0"/>
        </radialGradient>
        <filter id="edge-shadow" x="-10%" y="-10%" width="120%" height="120%">
          <feGaussianBlur stdDeviation="6"/>
        </filter>
      </defs>
      <path d="M792,0 C718,130 690,280 701,361 C712,500 756,630 809,703 L1173,703 L1173,0 Z"
            fill="#2a2a2a" filter="url(#edge-shadow)"/>
      <path d="M792,0 C718,130 690,280 701,361 C712,500 756,630 809,703 L1173,703 L1173,0 Z"
            fill="url(#silver-sheen)"/>
      <path d="M792,0 C718,130 690,280 701,361 C712,500 756,630 809,703 L1173,703 L1173,0 Z"
            fill="url(#silver-glow)"/>
    </svg>

    <section class="details">
      <h1 class="business-name">Willowmere Rites Studio</h1>
      <p class="tagline">"Crafting singular, bespoke<br>occasions honouring journeys"</p>
      <h2 class="person-name">Tamsin Crowther</h2>
      <p class="email">willowmereritesstudio1@quillpost.net</p>
      <p class="phone">0492-718305</p>
    </section>

    <aside class="brand-mark">
      <span class="brand-dot"></span>
      <p class="brand-name">Willowmere Rites<br>Studio</p>
    </aside>
  </main>
</body>
</html>
```